Stonebridge 720 Real Estate Investment Company

We need a business card designed for a real estate investment company named Stonebridge 720. We want to use red#f04a50, orange #f37122 and yellow #fbee3e as the color scheme. The logo colors will need to be modified from the current blue palette. I've attach VitalBranchly logo example that captures the color scheme we're going for for Stonebridge 720. Looking for clean Sans Serif fonts.
Contact Information for Business Card
Daniel Whitlock
Managing Partner
48613 Kessler Lane, Suite 540
Tampa, FL 33671
813-555-8740 Mobile
dwhitlock@stonebridge720.example
www.stonebridge720.example
Requirements
Must have
- Looking for creative responses.
Nice to have
- Must hit color palette... orange, red, yellow

```html
<!DOCTYPE html>
<html lang="en">
<head>
<meta charset="utf-8">
<title>Stonebridge 720 — Business Card</title>
<link rel="stylesheet" href="https://fonts.googleapis.com/css2?family=Lato:wght@400;700&family=Oswald:wght@500;600&display=swap">
<style>
  :root {
    --stage: #2a2a2a;
    --card-dark: #1e1e1e;
    --card-light: #ffffff;
    --ink: #1c1c1c;
    --ink-soft: #2e2e2e;
    --brand-red: #f04a50;
    --brand-orange: #f37122;
    --brand-yellow: #fbee3e;
    --white: #ffffff;
  }
  * { margin: 0; padding: 0; box-sizing: border-box; }
  html, body {
    width: 1200px; height: 900px; overflow: hidden;
    background: var(--stage);
    font-family: "Lato", sans-serif;
  }
  .sheet {
    position: relative; width: 1200px; height: 900px;
    display: flex; flex-direction: column; align-items: center;
    justify-content: center; gap: 36px;
  }
  .card {
    position: relative; width: 700px; height: 400px;
    box-shadow: 0 14px 30px rgba(0,0,0,.45);
    overflow: hidden;
  }
  .card--front {
    background: radial-gradient(ellipse at 75% 75%, #3a3a3a 0%, var(--card-dark) 60%);
    display: flex; align-items: center; justify-content: center;
  }
  .card--back { background: var(--card-light); color: var(--ink); }

  .wordmark {
    display: flex; align-items: center; gap: 14px;
    font-family: "Oswald", sans-serif; font-weight: 600;
    letter-spacing: .5px; line-height: 1; white-space: nowrap;
  }
  .wordmark__dot { width: 22px; height: 22px; border-radius: 50%; background: var(--brand-orange); }
  .card--front .wordmark { font-size: 52px; color: var(--white); }
  .card--back .wordmark {
    position: absolute; left: 0; right: 0; top: 58px;
    justify-content: center;
    font-size: 44px; color: var(--ink);
  }

  .holder {
    position: absolute; right: 380px; top: 192px; text-align: right;
    white-space: nowrap;
  }
  .holder__name {
    font-family: "Oswald", sans-serif; font-weight: 500;
    font-size: 34px; letter-spacing: 1px; color: var(--brand-red);
    text-transform: uppercase; line-height: 1.1;
  }
  .holder__title { font-size: 20px; color: var(--ink-soft); }

  .divider {
    position: absolute; left: 338px; top: 194px;
    width: 2px; height: 74px; background: var(--brand-orange);
  }

  .contact {
    position: absolute; left: 356px; top: 198px;
    list-style: none; font-size: 17px; color: var(--ink-soft);
    white-space: nowrap;
  }
  .contact__item { display: flex; align-items: center; gap: 9px; height: 24px; }
  .contact__icon { width: 13px; height: 13px; flex: none; }

  .address {
    position: absolute; left: 0; right: 0; top: 318px;
    text-align: center; font-size: 20px; color: var(--ink);
  }
</style>
</head>
<body>
<main class="sheet">
  <section class="card card--front" aria-label="Card front">
    <div class="wordmark"><span class="wordmark__dot"></span><span>Stonebridge 720</span></div>
  </section>

  <section class="card card--back" aria-label="Card back">
    <div class="wordmark"><span class="wordmark__dot"></span><span>Stonebridge 720</span></div>

    <div class="holder">
      <h1 class="holder__name">Daniel Whitlock</h1>
      <p class="holder__title">Managing Partner</p>
    </div>

    <div class="divider"></div>

    <ul class="contact">
      <li class="contact__item">
        <svg class="contact__icon" viewBox="0 0 16 16" aria-hidden="true"><path d="M4 1l3 3-2 2c1 2 3 4 5 5l2-2 3 3-2 3C7 15 1 9 1 4z" fill="var(--brand-red)"/></svg>
        813-555-8740
      </li>
      <li class="contact__item">
        <svg class="contact__icon" viewBox="0 0 16 16" aria-hidden="true"><rect x="1" y="3" width="14" height="10" fill="none" stroke="var(--brand-red)" stroke-width="1.5"/><path d="M1 3l7 6 7-6" fill="none" stroke="var(--brand-red)" stroke-width="1.5"/></svg>
        dwhitlock@stonebridge720.example
      </li>
      <li class="contact__item">
        <svg class="contact__icon" viewBox="0 0 16 16" aria-hidden="true"><circle cx="8" cy="8" r="6.5" fill="none" stroke="var(--brand-red)" stroke-width="1.4"/><ellipse cx="8" cy="8" rx="2.8" ry="6.5" fill="none" stroke="var(--brand-red)" stroke-width="1.2"/><path d="M1.5 8h13" stroke="var(--brand-red)" stroke-width="1.2"/></svg>
        www.stonebridge720.example
      </li>
    </ul>

    <p class="address">48613 Kessler Lane, Suite 540 Tampa, FL 33671</p>
  </section>
</main>
</body>
</html>
```